Hi,

I would like to have a invitation made for a party. exactly like the picture in the link below.

http://pinboardia.example/pin/730215948361027459/

However, Please change the colors into fun/ girly feeling. font can be different and size of the card should be the same

Name of the girl: RINA
What: Bachelorette Party
Where:TOLO Boat
Dubai Coral Quay Sailing Club
When:7th of February 2013

No RSVP required. (so no need to put it)

```html
<!DOCTYPE html>
<html lang="en">
<head>
<meta charset="utf-8">
<title>Rina's Bachelorette Party Invitation</title>
<link rel="stylesheet" href="https://fonts.googleapis.com/css2?family=Emilys+Candy&family=Love+Ya+Like+A+Sister&family=Train+One&family=Della+Respira&display=swap">
<style>
  :root {
    --paper: #ffffff;
    --rose: #f06283;
    --blush: #f7c0cf;
    --wine: #7b1320;
    --cream: #fde3b5;
    --magenta: #e0168b;
    --petal: #f9b4c6;
    --fold: #e0679a;
  }
  * { margin: 0; padding: 0; box-sizing: border-box; }
  html, body {
    width: 1200px; height: 663px; overflow: hidden;
    background: var(--paper);
  }
  .invitation {
    position: relative;
    width: 1200px; height: 663px;
    background: var(--paper);
  }
  .fold-marks {
    position: absolute; inset: 0;
    pointer-events: none;
  }
  .cover {
    position: absolute;
    left: 73px; top: 80px;
    width: 700px; height: 506px;
    background: var(--rose);
  }
  .details {
    position: absolute;
    left: 773px; top: 80px;
    width: 355px; height: 506px;
    background: var(--blush);
  }
  .ornament {
    position: absolute;
    border-radius: 50%;
  }
  .ornament--heart-top {
    left: 360px; top: 92px; width: 58px; height: 40px;
    background: var(--petal); opacity: .55;
  }
  .ornament--heart-bottom {
    left: 83px; top: 540px; width: 58px; height: 40px;
    background: var(--petal); opacity: .55;
  }
  .ornament--flourish {
    left: 438px; top: 205px; width: 300px; height: 58px;
    border-radius: 40px;
    background: linear-gradient(90deg, rgba(123,19,32,0), rgba(123,19,32,.35) 50%, rgba(123,19,32,0));
  }
  .ornament--frame {
    left: 803px; top: 86px; width: 296px; height: 494px;
    border-radius: 60px;
    background: radial-gradient(ellipse at center, rgba(123,19,32,0) 62%, rgba(123,19,32,.22) 100%);
  }
  .headline {
    position: absolute; left: 0; top: 0;
    width: 1200px; height: 663px;
    overflow: visible;
  }
  .headline__name {
    font-family: "Emilys Candy", cursive;
    fill: var(--wine);
    font-size: 84px;
  }
  .headline__tagline {
    font-family: "Love Ya Like A Sister", cursive;
    fill: var(--cream);
    font-size: 44px;
  }
  .headline__single {
    font-family: "Train One", sans-serif;
    fill: var(--paper);
    font-size: 262px;
  }
  .event-info {
    position: absolute;
    left: 773px; top: 80px; width: 355px;
    text-align: center;
    font-family: "Della Respira", serif;
  }
  .event-info__item { position: absolute; left: 0; width: 355px; }
  .event-info__label {
    color: var(--magenta);
    font-size: 25px; line-height: 28px;
  }
  .event-info__value {
    color: var(--wine);
    font-size: 16px; line-height: 21px;
  }
</style>
</head>
<body>
<main class="invitation">
  <svg class="fold-marks" width="1200" height="663" aria-hidden="true">
    <line x1="426" y1="28" x2="426" y2="625" stroke="var(--fold)" stroke-width="1" stroke-dasharray="3 3"/>
    <line x1="773" y1="28" x2="773" y2="625" stroke="var(--fold)" stroke-width="1" stroke-dasharray="3 3"/>
  </svg>

  <section class="cover" aria-label="Invitation cover"></section>
  <section class="details" aria-label="Party details"></section>

  <div class="ornament ornament--heart-top" role="img" aria-label="Small outlined heart decoration"></div>
  <div class="ornament ornament--heart-bottom" role="img" aria-label="Small outlined heart decoration"></div>
  <div class="ornament ornament--flourish" role="img" aria-label="Swirling flourish with a heart"></div>
  <div class="ornament ornament--frame" role="img" aria-label="Scrolled frame with hearts around the party details"></div>

  <svg class="headline" width="1200" height="663" role="heading" aria-level="1">
    <text class="headline__name" x="101" y="265" textLength="315" lengthAdjust="spacingAndGlyphs">RINA’S</text>
    <text class="headline__tagline" x="106" y="324" textLength="657" lengthAdjust="spacingAndGlyphs">LAST CHANCE TO CELEBRATE BEING</text>
    <text class="headline__single" x="91" y="541" textLength="672" lengthAdjust="spacingAndGlyphs">SINGLE</text>
  </svg>

  <section class="event-info">
    <div class="event-info__item" style="top:90px">
      <p class="event-info__label">Name of the girl:</p>
      <p class="event-info__value">RINA</p>
    </div>
    <div class="event-info__item" style="top:183px">
      <p class="event-info__label">What:</p>
      <p class="event-info__value">Bachelorette Party</p>
    </div>
    <div class="event-info__item" style="top:272px">
      <p class="event-info__label">Where:</p>
      <p class="event-info__value">TOLO Boat<br>Dubai Coral Quay Sailing Club</p>
    </div>
    <div class="event-info__item" style="top:379px">
      <p class="event-info__label">When:</p>
      <p class="event-info__value">7th of February 2013</p>
    </div>
  </section>
</main>
</body>
</html>
```